Corporate marketing website with signup form

The function of the website is to promote our 2 product offerings. It will contain a main screen and several 5-7 sub-pages that will be available as 'scroll down' anchors and as front-page navigation links on the top of the page.

Navigation menu labels are: Products, Unique Model, Pricing, About, and Contact

Target Market(s)

Business to business marketers who are looking to source lead generation services

Industry/Entity Type

Marketing

Logo Text

Lumavex

Coding

Coded - Design and coding required

Number of Pages Required

5+ page

Requirements
Must have
• A sign-up form on main section of the front page. Fields are First Name, Last Name, Company, and Email (all text), and a pull-down with three options (only pick one): Track 1, Track 2, Custom Combination.
• Also incorporate the bottom half (ie crop the image) of the EPS file attached (the 'blue heads). Add this to the lower portion of the main screen and have the rest of the blue background become the background for the next anchored section of the navigation.
• You'll see the main section text in the mock-up I provided. The rest of the menu items/anchors can be lorem ipsum for now.
• Can this be coded in Wordpress? That would be my preference so I can edit it in the future.

```html
<!DOCTYPE html>
<html lang="en">
<head>
<meta charset="utf-8">
<title>Lumavex — List and Audience Building</title>
<link href="https://fonts.googleapis.com/css2?family=Montserrat:wght@400;600;700&family=Open+Sans:wght@400;600;700&display=swap" rel="stylesheet">
<style>
:root{
  --orange:#f47b20;
  --blue:#1491ee;
  --blue-deep:#0e6fc4;
  --navy:#14507e;
  --ink:#333a40;
  --muted:#7b858c;
  --gray-band:#d9dbdd;
  --line:#e3e6e9;
  --white:#ffffff;
  --red:#e4131b;
  --green:#39b54a;
  --gold:#f7c600;
  --teal:#16b6c2;
}
*{box-sizing:border-box;margin:0;padding:0}
html,body{width:1200px;height:2472px;overflow:hidden}
body{position:relative;background:var(--white);font-family:"Open Sans",Arial,sans-serif;color:var(--ink)}
a{color:inherit;text-decoration:none}

/* header */
.site-header{position:absolute;top:0;left:0;width:1200px;height:58px;background:var(--white);display:flex;align-items:center;padding:0 30px;z-index:3}
.brand{display:flex;align-items:center;gap:10px;font-family:"Montserrat",sans-serif;font-weight:700;font-size:26px;color:var(--orange)}
.brand-dot{width:34px;height:34px;border-radius:50%;background:var(--orange)}
.phone{margin-left:120px;display:flex;align-items:center;gap:6px;font-size:13px;color:var(--blue-deep)}
.main-nav{margin-left:auto;display:flex;gap:6px}
.main-nav a{font-size:12px;font-weight:600;letter-spacing:.5px;color:var(--muted);padding:9px 16px;text-transform:uppercase}
.main-nav a.active{background:var(--blue);color:var(--white)}

/* hero */
.hero{position:absolute;top:58px;left:0;width:1200px;height:602px}
.hero-photo{position:absolute;inset:0;background:linear-gradient(100deg,#e9eef3 0%,#c9d6e1 45%,#8ea2b6 75%,#55687e 100%)}
.hero-title{position:absolute;left:140px;top:290px;font-family:"Montserrat",sans-serif;font-weight:600;font-size:30px;line-height:40px;color:#2c3640;text-transform:uppercase}
.hero-arrow{position:absolute;top:298px;width:24px;height:40px}
.hero-arrow.prev{left:22px}.hero-arrow.next{right:22px}

/* tracks */
.tracks{position:absolute;top:660px;left:0;width:1200px;height:520px;background:linear-gradient(#f2f3f4,var(--gray-band))}
.track-card{position:absolute;top:80px;height:420px;background:var(--white);box-shadow:0 10px 18px rgba(0,0,0,.18)}
.track-card.one{left:148px;width:280px}
.track-card.two{left:452px;width:288px}
.track-card.form{left:764px;width:296px}
.card-head{height:64px;background:var(--orange);color:var(--white);text-align:center;font-family:"Montserrat",sans-serif;font-weight:700;font-size:13px;letter-spacing:.5px;padding-top:8px}
.card-head svg{display:block;margin:0 auto 6px}
.card-list{list-style:none;padding:16px 16px 0}
.card-list li{display:flex;gap:10px;font-size:10.5px;line-height:15px;color:var(--muted);margin-bottom:16px}
.card-list li svg{flex:none}
.coming-soon{position:absolute;left:16px;right:16px;bottom:22px;background:var(--blue);color:var(--white);padding:10px 12px;font-size:10px;line-height:14px}
.coming-soon strong{display:block;font-size:11px;margin-bottom:3px}
.signup-form{padding:12px 16px 0}
.signup-form label{display:block;font-size:10px;color:var(--ink);margin-bottom:3px}
.signup-form .field{height:24px;border:1px solid var(--line);margin-bottom:10px;font-size:10px;color:#aab2b8;padding:5px 7px}
.signup-form .select{width:80px;display:flex;justify-content:space-between;align-items:center;color:var(--ink)}
.submit{display:block;width:100%;height:28px;background:var(--blue);color:var(--white);border:0;font-size:11px;font-weight:700;letter-spacing:.5px;margin-top:4px}

/* pricing */
.pricing{position:absolute;top:1180px;left:0;width:1200px;height:660px}
.section-title{font-family:"Montserrat",sans-serif;font-weight:700;font-size:28px;letter-spacing:1px;text-align:center}
.pricing .section-title{position:absolute;top:104px;width:100%;color:var(--blue)}
.plan{position:absolute;top:200px;height:400px;background:var(--white);box-shadow:0 4px 12px rgba(0,0,0,.12);text-align:center}
.plan.basic{left:148px;width:192px}
.plan.featured{left:352px;top:172px;height:428px;width:240px;z-index:1}
.plan.gold{left:600px;width:240px}
.plan.premium{left:852px;width:208px}
.plan-name{height:56px;line-height:56px;color:var(--white);font-family:"Montserrat",sans-serif;font-weight:700;font-size:20px;letter-spacing:.5px}
.basic .plan-name{background:var(--red)}
.featured .plan-name{background:var(--green);height:72px;line-height:72px}
.gold .plan-name{background:var(--gold)}
.premium .plan-name{background:var(--teal)}
.plan-row{height:48px;line-height:48px;border-bottom:1px solid var(--line);font-size:15px}
.plan-row.price{font-size:24px;height:60px;line-height:60px}
.plan-btn{position:absolute;bottom:20px;left:50%;transform:translateX(-50%);width:124px;height:34px;line-height:34px;background:var(--navy);color:var(--white);font-size:13px;letter-spacing:.5px}

/* products */
.heads-band{position:absolute;top:1830px;left:0;width:1200px;height:70px;background:linear-gradient(var(--white),var(--blue))}
.products{position:absolute;top:1900px;left:0;width:1200px;height:360px;background:var(--blue)}
.products .section-title{padding-top:40px;color:var(--white)}
.product-image{position:absolute;left:212px;top:100px;width:228px;height:228px;border-radius:50%;background:radial-gradient(circle at 50% 45%,#eef3f8,#a9c3dd)}
.product-copy{position:absolute;left:432px;top:104px;width:520px;color:var(--white)}
.product-copy h3{font-size:16px;font-weight:700;margin-bottom:10px}
.product-copy p{font-size:11px;line-height:17px}
.read-more{display:inline-block;margin-top:14px;background:var(--orange);font-size:11px;font-weight:700;padding:6px 16px}
.slider-dots{position:absolute;left:580px;top:292px;display:flex;gap:14px}

/* footer */
.site-footer{position:absolute;top:2260px;left:0;width:1200px;height:212px;text-align:center}
.site-footer .brand{justify-content:center;margin-top:34px}
.footer-nav{margin-top:30px;font-size:13px;color:var(--ink)}
.footer-nav span{margin:0 8px;color:var(--muted)}
.copyright{margin-top:10px;font-size:12px;color:var(--muted)}
</style>
</head>
<body>

<header class="site-header">
  <a class="brand" href="#"><span class="brand-dot"></span>Lumavex</a>
  <span class="phone">
    <svg width="12" height="12" viewBox="0 0 24 24"><path fill="#0e6fc4" d="M6.6 10.8a15 15 0 0 0 6.6 6.6l2.2-2.2c.3-.3.7-.4 1-.2 1.1.4 2.3.6 3.6.6.6 0 1 .4 1 1V20c0 .6-.4 1-1 1A17 17 0 0 1 3 4c0-.6.4-1 1-1h3.5c.6 0 1 .4 1 1 0 1.3.2 2.5.6 3.6.1.3 0 .7-.2 1z"/></svg>
    555-204-7810
  </span>
  <nav class="main-nav">
    <a class="active" href="#">Home</a>
    <a href="#products">Products</a>
    <a href="#">Unique Model</a>
    <a href="#pricing">Pricing</a>
    <a href="#">About</a>
    <a href="#">Contact</a>
  </nav>
</header>

<section class="hero">
  <div class="hero-photo" role="img" aria-label="City skyline with a businessman in a suit on the right"></div>
  <h1 class="hero-title">List and audience building for<br>your content marketing efforts</h1>
  <svg class="hero-arrow prev" viewBox="0 0 24 40"><path d="M18 6 6 20l12 14" fill="none" stroke="#fff" stroke-width="4"/></svg>
  <svg class="hero-arrow next" viewBox="0 0 24 40"><path d="M6 6l12 14L6 34" fill="none" stroke="#fff" stroke-width="4"/></svg>
</section>

<section class="tracks">
  <article class="track-card one">
    <div class="card-head">
      <svg width="22" height="22" viewBox="0 0 24 24"><rect x="3" y="3" width="18" height="18" rx="3" fill="none" stroke="#fff" stroke-width="2"/><path d="M12 7v10M7 12h10" stroke="#fff" stroke-width="2"/></svg>
      TRACK 1
    </div>
    <ul class="card-list">
      <li><svg width="18" height="18" viewBox="0 0 24 24"><circle cx="12" cy="12" r="11" fill="#1491ee"/><path d="m7 12 3 3 7-7" fill="none" stroke="#fff" stroke-width="2"/></svg>Collect in-house or upload your existing prospect database</li>
      <li><svg width="18" height="18" viewBox="0 0 24 24"><circle cx="12" cy="12" r="11" fill="#1491ee"/><path d="m7 12 3 3 7-7" fill="none" stroke="#fff" stroke-width="2"/></svg>Give us your ideal target roles, company size and industry</li>
      <li><svg width="18" height="18" viewBox="0 0 24 24"><circle cx="12" cy="12" r="11" fill="#1491ee"/><path d="m7 12 3 3 7-7" fill="none" stroke="#fff" stroke-width="2"/></svg>We provide contact lists derived from real-time data for your target</li>
    </ul>
    <div class="coming-soon"><strong>Coming Soon</strong>Enhanced engagement and intent signals for deeper targeting in each list you buy.</div>
  </article>

  <article class="track-card two">
    <div class="card-head">
      <svg width="22" height="22" viewBox="0 0 24 24"><rect x="3" y="3" width="18" height="18" rx="3" fill="none" stroke="#fff" stroke-width="2"/><path d="M8 9h8M8 13h8M8 17h5" stroke="#fff" stroke-width="2"/></svg>
      TRACK 2
    </div>
    <ul class="card-list">
      <li><svg width="18" height="18" viewBox="0 0 24 24"><circle cx="12" cy="12" r="11" fill="#1491ee"/><path d="M6 8h12v8H6zM6 8l6 5 6-5" fill="none" stroke="#fff" stroke-width="1.6"/></svg>We use our data and email domains to send campaigns for you</li>
      <li><svg width="18" height="18" viewBox="0 0 24 24"><circle cx="12" cy="12" r="11" fill="#1491ee"/><path d="M7 17V11M12 17V7M17 17v-4" stroke="#fff" stroke-width="2"/></svg>You get access to all the campaign reports each week and pay for actions</li>
    </ul>
  </article>

  <article class="track-card form">
    <div class="card-head">
      <svg width="22" height="22" viewBox="0 0 24 24"><rect x="4" y="3" width="16" height="18" rx="2" fill="none" stroke="#fff" stroke-width="2"/><path d="M8 8h8M8 12h8M8 16h5" stroke="#fff" stroke-width="2"/></svg>
      I WANT TO LEARN MORE
    </div>
    <form class="signup-form">
      <label>First Name</label><div class="field">First name</div>
      <label>Last Name</label><div class="field">Last name</div>
      <label>E-mail</label><div class="field">Email address</div>
      <div class="field select">Track 1<svg width="8" height="6" viewBox="0 0 8 6"><path d="M0 0h8L4 6z" fill="#333a40"/></svg></div>
      <label>Company</label><div class="field">Company name</div>
      <button class="submit" type="button">SUBMIT</button>
    </form>
  </article>
</section>

<section class="pricing" id="pricing">
  <h2 class="section-title">PRICING</h2>
  <div class="plan basic"><div class="plan-name">BASIC</div><div class="plan-row price">$20</div><div class="plan-row">Lorium ipsum</div><div class="plan-row">Dolor Amit</div><div class="plan-row">Seu edrty foundation</div><a class="plan-btn" href="#">SIGN UP</a></div>
  <div class="plan featured"><div class="plan-name">FEATURED</div><div class="plan-row price">$20</div><div class="plan-row">Lorium ipsum</div><div class="plan-row">Dolor Amit</div><div class="plan-row">Seu edrty foundation</div><a class="plan-btn" href="#">SIGN UP</a></div>
  <div class="plan gold"><div class="plan-name">GOLD</div><div class="plan-row price">$20</div><div class="plan-row">Lorium ipsum</div><div class="plan-row">Dolor Amit</div><div class="plan-row">Seu edrty foundation</div><a class="plan-btn" href="#">SIGN UP</a></div>
  <div class="plan premium"><div class="plan-name">PREMIUM</div><div class="plan-row price">$20</div><div class="plan-row">Lorium ipsum</div><div class="plan-row">Dolor Amit</div><div class="plan-row">Seu edrty foundation</div><a class="plan-btn" href="#">SIGN UP</a></div>
</section>

<div class="heads-band" role="img" aria-label="Row of blue head silhouettes rising into the blue section"></div>

<section class="products" id="products">
  <h2 class="section-title">PRODUCTS</h2>
  <div class="product-image" role="img" aria-label="Hand holding a network of connected people icons"></div>
  <div class="product-copy">
    <h3>Sed ut perspiciatis unde</h3>
    <p>Lorem ipsum dolor sit amet, consectetur adipiscing elit, sed do eiusmod tempor incididunt ut labore et dolore magna aliqua. Ut enim ad minim veniam, quis nostrud exercitation ullamco laboris nisi ut aliquip ex ea commodo consequat. Duis aute irure dolor in reprehenderit in voluptate velit esse cillum dolore.</p>
    <a class="read-more" href="#">READ MORE</a>
  </div>
  <div class="slider-dots">
    <svg width="10" height="14" viewBox="0 0 10 14"><path d="M8 1 2 7l6 6" fill="none" stroke="#fff" stroke-width="2"/></svg>
    <svg width="10" height="14" viewBox="0 0 10 14"><path d="m2 1 6 6-6 6" fill="none" stroke="#fff" stroke-width="2"/></svg>
  </div>
</section>

<footer class="site-footer">
  <a class="brand" href="#"><span class="brand-dot"></span>Lumavex</a>
  <nav class="footer-nav">Home<span>|</span>Products<span>|</span>Unique Model<span>|</span>Pricing<span>|</span>About<span>|</span>Contact</nav>
  <p class="copyright">© 2016 Company Name | All Rights Reserved</p>
</footer>

</body>
</html>
```